Business Cards for a company that provides webstore services to veterinarians

We need business cards designed for our main service PawCartHub. PawCartHub is a webstore that veterinarian clinics can use to that will allow their clients to purchase products for their pets. Our company is Brindlow Veterinary Solutions (Brindlow Veterinary Solutions). Our mission statement is We love pets! We will do everything possible to facilitate along, healthy and happy relationship with their families.

Target Market(s)

Veterinarians

Industry/Entity Type

Veterinary

Contact Information for Business Card

I would like the design to incorporate the colours our our company. Cards should have room for employee name, title (only necessary in two instances), phone number, mobile number, email address and linkedin symbol and related profile name ie Marla Quinton. I would like the PawCartHub logo to appear on one side and Brindlow Veterinary Solutions logo to appear on the other. I will need both an english and french version. I can provide the french translation. Please focus on english version and then we will translate

Colors

Designer to choose colors to be used in the design.

Requirements
Must have
• one side - PawCartHub logo with persons name, phone number, mobile number, email address
• second side - Brindlow Veterinary Solutions logo
• colours should be consistent with our company. colours are as follows:
• Red
• RGB: 190 / 30 / 45
• CYMK: 14 / 100 / 90 /10
• Hex: #BE1E2D
• Gray
• RGB: 88 / 89 / 86
• CYMK: 3 / 2 / 0 /64
• Hex: #585956
Nice to have
• address of company - can be on either side address is 4817 Feldmoor Street Suite 305 Burlington ON K2R 6T4. Toll free number will vary depending on person
• plain circle symbol and name of person
• on second side with Brindlow Veterinary Solutions logo our company's mission statement
Should not have
• nothing comes to mind

```html
<!DOCTYPE html>
<html lang="en">
<head>
<meta charset="utf-8">
<title>PawCartHub / Brindlow Veterinary Solutions Business Cards</title>
<link rel="stylesheet" href="https://fonts.googleapis.com/css2?family=Source+Sans+3:wght@400;600;700&display=swap">
<style>
  :root {
    --brand-red: #be1e2d;
    --brand-gray: #585956;
    --stage: #1b1b1b;
    --card-light: #f2f2f2;
    --ink: #1e1e1e;
    --white: #ffffff;
  }
  * { margin: 0; padding: 0; box-sizing: border-box; }
  html, body {
    width: 1200px; height: 900px; overflow: hidden;
    background: var(--stage);
    font-family: "Source Sans 3", Arial, sans-serif;
  }
  .canvas { position: relative; width: 1200px; height: 900px; }
  .card {
    position: absolute; top: 170px;
    width: 347px; height: 561px; overflow: hidden;
    text-align: center;
  }
  .card--front { left: 259px; background: var(--card-light); color: var(--ink); }
  .card--back { left: 631px; background: var(--brand-red); color: var(--white); }

  .wordmark {
    position: absolute; top: 128px; left: 0; width: 100%;
    font-size: 44px; font-weight: 600; letter-spacing: -0.5px;
    color: var(--brand-gray);
  }
  .person { position: absolute; top: 299px; left: 0; width: 100%; }
  .person__name {
    font-size: 20px; font-weight: 600; letter-spacing: 0.4px;
    color: var(--brand-red); text-transform: uppercase; line-height: 24px;
  }
  .person__title { font-size: 16px; line-height: 20px; }
  .contacts { margin-top: 21px; font-size: 16px; line-height: 20.5px; }
  .contacts__label { color: var(--brand-red); font-weight: 700; }
  .address { margin-top: 8px; font-size: 16px; line-height: 20.5px; }

  .footer-band {
    position: absolute; left: 0; bottom: 0; width: 100%; height: 59px;
    background: var(--brand-red);
  }
  .profile-dot {
    position: absolute; left: 137px; top: 497px;
    width: 74px; height: 74px; border-radius: 50%;
    background: var(--white);
  }

  .company-name {
    position: absolute; top: 200px; left: 0; width: 100%;
    font-size: 40px; font-weight: 600; line-height: 46px;
  }
  .mission {
    position: absolute; top: 446px; left: 0; width: 100%;
    font-size: 16px; line-height: 20.5px;
  }
</style>
</head>
<body>
<main class="canvas">
  <section class="card card--front" aria-label="Business card front">
    <div class="wordmark">PawCartHub</div>
    <div class="person">
      <p class="person__name">Daniel Harrow</p>
      <p class="person__title">Managing Director</p>
      <div class="contacts">
        <p><span class="contacts__label">P:</span> (044)555018273</p>
        <p><span class="contacts__label">M:</span> (044)555018273</p>
        <p><span class="contacts__label">E:</span> info@pawcarthub.ca</p>
      </div>
      <div class="address">
        <p>4817 Feldmoor Street Suite 305</p>
        <p>Burlington ON K2R 6T4</p>
      </div>
    </div>
    <div class="footer-band"></div>
    <div class="profile-dot" aria-label="Profile link"></div>
  </section>

  <section class="card card--back" aria-label="Business card back">
    <div class="company-name">
      <p>Brindlow</p>
      <p>Veterinary</p>
      <p>Solutions</p>
    </div>
    <div class="mission">
      <p>We love pets!</p>
      <p>We will do everything possible to</p>
      <p>facilitate along, healthy and happy</p>
      <p>relationship with their families.</p>
    </div>
  </section>
</main>
</body>
</html>
```